Kip's Pharmacy Business Card Design Project

I need a business card designed for my pharmacy Kip's Pharmacy. I would like just the logo on one side, maybe with black background and white lettering. The other side I would also like to include my logo which is attached. Also, please include my name and the following information:
Rolf Mayhew Owner/Pharm D.
Business address is 7314 N Birchwood Rd Sioux Falls, SD 57193.
Phone number is 605-318-2067 and fax # is 605-318-2063.
my email address is kip@kipsrxhall.com.
My website is www.kipsrxhall.com.
My business hours are Monday-Friday 8am-7 pm. Saturday 8am-12 pm. Sunday Closed.
I would like the design to include my logo colors, black, white, and neon green. Silver may be added as a highlight. Thanks.
Industry/Entity Type
Pharmacy
Contact Information for Business Card
See above in product description
Look and feel

```html
<!DOCTYPE html>
<html lang="en">
<head>
<meta charset="utf-8">
<title>Kip's Pharmacy – Business Card</title>
<link rel="stylesheet" href="https://fonts.googleapis.com/css2?family=Open+Sans:wght@400;600&display=swap">
<style>
  :root {
    --ink: #3a3a3c;
    --ink-deep: #2b2b2d;
    --paper: #ffffff;
    --stage: #ebebeb;
    --red: #d9202f;
    --orange: #f07a22;
    --green: #8dc63f;
    --blue: #1296d8;
    --blue-fold: #0b6a9c;
    --text-dark: #333335;
    --text-light: #ffffff;
    --muted: #d8d8d8;
  }
  * { box-sizing: border-box; margin: 0; padding: 0; }
  html, body { width: 1200px; height: 900px; overflow: hidden; }
  body {
    background: var(--stage);
    font-family: "Open Sans", Arial, sans-serif;
    position: relative;
  }
  .card {
    position: absolute;
    width: 620px;
    height: 354px;
    background: var(--paper);
    box-shadow: 0 6px 18px rgba(0,0,0,.18);
    overflow: hidden;
  }
  .card--front { left: 100px; top: 70px; }
  .card--back  { left: 480px; top: 476px; }

  /* ---------- front ---------- */
  .front-band-left {
    position: absolute; left: 0; top: 0; width: 48px; height: 100%;
    background: var(--ink);
  }
  .front-band-top {
    position: absolute; right: 0; top: 0; width: 70px; height: 150px;
    background: var(--ink);
  }
  .tab-stack { position: absolute; display: flex; flex-direction: column; }
  .tab-stack span { display: block; }
  .tab-stack--left { left: 22px; top: 70px; width: 86px; }
  .tab-stack--left span { height: 46px; }
  .tab-stack--right { right: 20px; top: 0; width: 64px; }
  .tab-stack--right span { height: 30px; }
  .fill-red { background: var(--red); }
  .fill-orange { background: var(--orange); }
  .fill-green { background: var(--green); }
  .fill-blue { background: var(--blue); }
  .tab-fold {
    position: absolute; width: 0; height: 0;
    border-top: 14px solid var(--blue-fold);
    border-left: 14px solid transparent;
  }
  .tab-stack--left + .tab-fold { left: 94px; top: 254px; }

  .brand {
    position: absolute;
    display: flex; align-items: center; gap: 16px;
    color: var(--text-dark);
    font-weight: 600;
  }
  .brand-dot {
    width: 30px; height: 30px; border-radius: 50%;
    background: var(--green);
  }
  .brand-rule { width: 1px; height: 46px; background: currentColor; opacity: .6; }
  .card--front .brand { left: 190px; top: 150px; font-size: 30px; }

  .hours {
    position: absolute; left: 170px; bottom: 26px;
    font-size: 15px; color: var(--text-dark);
  }

  /* ---------- back ---------- */
  .back-panel {
    position: absolute; left: 0; top: 0; width: 382px; height: 100%;
    background: var(--ink);
  }
  .card--back .brand {
    left: 28px; top: 112px; font-size: 24px; color: var(--text-light); gap: 12px;
  }
  .card--back .brand-dot { width: 24px; height: 24px; }
  .card--back .brand-rule { height: 36px; }
  .holder {
    position: absolute; left: 120px; top: 160px;
    color: var(--text-light); text-align: center; line-height: 1.15;
  }
  .holder-name { font-size: 21px; }
  .holder-role { font-size: 14px; color: var(--muted); }

  .icon-tabs {
    position: absolute; left: 322px; top: 52px; width: 60px;
    display: flex; flex-direction: column; gap: 2px;
  }
  .icon-tab {
    height: 60px; display: flex; align-items: center; justify-content: center;
  }
  .icon-tab svg { width: 26px; height: 26px; fill: #fff; }
  .icon-tabs + .tab-fold { left: 322px; top: 298px; border-top-color: var(--blue-fold); border-left: 0; border-right: 12px solid transparent; }

  .contact {
    position: absolute; left: 404px; top: 52px; width: 210px;
    color: var(--text-dark); font-size: 13px; line-height: 1.3;
  }
  .contact-row { height: 62px; display: flex; flex-direction: column; justify-content: center; }
  .contact-name { font-size: 15px; }
  .contact-role { font-size: 12px; color: #666; }
</style>
</head>
<body>

<section class="card card--front" aria-label="Card front">
  <div class="front-band-left"></div>
  <div class="front-band-top"></div>
  <div class="tab-stack tab-stack--left">
    <span class="fill-red"></span><span class="fill-orange"></span>
    <span class="fill-green"></span><span class="fill-blue"></span>
  </div>
  <div class="tab-fold"></div>
  <div class="tab-stack tab-stack--right">
    <span class="fill-red"></span><span class="fill-orange"></span>
    <span class="fill-green"></span><span class="fill-blue"></span>
  </div>
  <div class="brand">
    <span class="brand-dot"></span>
    <span class="brand-rule"></span>
    <span class="brand-name">Kip's Pharmacy</span>
  </div>
  <p class="hours">Monday-Friday 8am-7 pm. Saturday 8am-12 pm</p>
</section>

<section class="card card--back" aria-label="Card back">
  <div class="back-panel"></div>
  <div class="brand">
    <span class="brand-dot"></span>
    <span class="brand-rule"></span>
    <span class="brand-name">Kip's Pharmacy</span>
  </div>
  <div class="holder">
    <p class="holder-name">Rolf Mayhew</p>
    <p class="holder-role">Owner/Pharm D</p>
  </div>

  <div class="icon-tabs">
    <div class="icon-tab fill-red">
      <svg viewBox="0 0 24 24" aria-hidden="true"><rect x="8" y="3" width="8" height="8" rx="1"/><path d="M3 21v-3c0-3 4-5 9-5s9 2 9 5v3z"/></svg>
    </div>
    <div class="icon-tab fill-orange">
      <svg viewBox="0 0 24 24" aria-hidden="true"><path d="M12 3 2 12h3v9h5v-6h4v6h5v-9h3z"/></svg>
    </div>
    <div class="icon-tab fill-green">
      <svg viewBox="0 0 24 24" aria-hidden="true"><path d="M3 8c0-2 4-4 9-4s9 2 9 4v2h-5V8H8v2H3z"/><path d="M6 11h12l2 9H4z"/></svg>
    </div>
    <div class="icon-tab fill-blue">
      <svg viewBox="0 0 24 24" aria-hidden="true"><path d="M12 2a10 10 0 1 0 0 20 10 10 0 0 0 0-20zm0 2c1 1.2 1.9 3.3 2.1 6H9.9C10.1 7.3 11 5.2 12 4zM4.1 11h3.8c.1 2.6.7 4.6 1.6 6.2A8 8 0 0 1 4.1 11zm0-1A8 8 0 0 1 9.5 4.8C8.6 6.3 8 8.2 7.9 10zm5.8 1h4.2c-.2 2.8-1.1 4.9-2.1 6-1-1.1-1.9-3.2-2.1-6zm6.2 0h3.8a8 8 0 0 1-5.4 6.2c.9-1.6 1.5-3.6 1.6-6.2zm0-1c-.1-1.8-.7-3.7-1.6-5.2A8 8 0 0 1 19.9 10z"/></svg>
    </div>
  </div>
  <div class="tab-fold"></div>

  <div class="contact">
    <div class="contact-row">
      <span class="contact-name">Rolf Mayhew</span>
      <span class="contact-role">Owner/Pharm D</span>
    </div>
    <div class="contact-row">
      <span>7314 N Birchwood Rd Sioux Falls,</span>
      <span>SD 57193</span>
    </div>
    <div class="contact-row">
      <span>605.318.2067</span>
      <span>605.318.2063</span>
    </div>
    <div class="contact-row">
      <span>kip@kipsrxhall.com</span>
      <span>www.kipsrxhall.com</span>
    </div>
  </div>
</section>

</body>
</html>
```